Refresh of far beyond ordinary IT house website

Our web site is starting to show it's age. You can see the existing site here: www.plumbrook.net. As a growing company we want to come across as a dynamic collection of IT experts.

We want to update the design so are open to any colour palette and look, but want to retain our current table logo. We use the logo on our business cards but with a white background - see the attached file, so you don't need to keep the brown or the green.

The design should consider the range of browsers that will be looking at the site - so please show how it will look on a wide screen laptop and a 768x1024 tablet.

We want to add some pages about our team and their skills, probably with photos of each person on the team.

This is an uncoded project - the PSD files of the design is required, not coding.
Updates

Thanks everyone for the submissions so far.  It's a holiday day in the UK today but we will get some feedback on the designs so far out to you.

Target Market(s)

Architects and other creative types looking for IT support

Industry/Entity Type

Business

Font styles to use
Serif
Sans Serif

Requirements
Must have
• Must look good on a laptop and an iPad.

```html
<!DOCTYPE html>
<html lang="en">
<head>
<meta charset="utf-8">
<title>Plumbrook – IT Services</title>
<link rel="stylesheet" href="https://fonts.googleapis.com/css2?family=Noto+Sans:wght@400;700&display=swap">
<style>
:root{
  --plum:#8e1a5a;
  --gold:#d9a700;
  --ink:#333;
  --muted:#666;
  --text-grey:#7a7a7a;
  --line:#dcdcdc;
  --panel:#efefef;
  --footer:#cbcbcb;
  --footer-dark:#5c5c5c;
  --btn-grey:#8a8a8a;
  --icon-dark:#666;
  --icon-blue:#4e6d9c;
}
*{box-sizing:border-box;margin:0;padding:0}
html,body{width:746px;height:1200px;overflow:hidden}
body{position:relative;background:#fff;font-family:"Noto Sans",Verdana,sans-serif;color:var(--ink)}
.abs{position:absolute}

/* top bar */
.topbar{left:0;top:0;width:746px;height:21px;background:var(--plum);color:#fff;font-size:9px}
.topbar .contact{left:54px;top:4px;display:flex;gap:10px;align-items:center}
.topbar .contact svg{vertical-align:-1px;margin-right:4px}
.topbar .phone{font-size:10px}
.btn-signin{left:616px;top:0;width:50px;height:21px;background:var(--gold);color:#fff;font-size:9px;text-align:center;line-height:21px}
.btn-signup{left:666px;top:0;width:51px;height:21px;background:#111;color:#fff;font-size:9px;text-align:center;line-height:21px}

/* header */
.header{left:0;top:21px;width:746px;height:73px;background:#f7f7f7}
.brand{left:52px;top:23px;display:flex;align-items:center;gap:20px}
.brand-mark{width:24px;height:24px;background:var(--gold)}
.brand-name{font-size:27px;font-weight:700;color:var(--plum);letter-spacing:.3px}
.search{left:582px;top:29px;width:132px;height:18px;border:1px solid #ccc;border-radius:9px;background:#fff;font-size:8px;color:#888;padding:4px 0 0 7px}
.search svg{position:absolute;right:6px;top:4px}

/* nav */
.nav{left:0;top:94px;width:746px;height:36px;background:linear-gradient(#e8e8e8,#d2d2d2);border-bottom:2px solid #bbb}
.nav ul{list-style:none;display:flex;position:absolute;left:44px;top:0;height:34px}
.nav li{font-size:9.5px;letter-spacing:.6px;color:#444;line-height:34px;padding:0 17px;border-right:1px solid #bdbdbd}
.nav li:last-child{border-right:none}
.social{display:flex;gap:5px}
.social span{width:17px;height:17px;border-radius:50%;background:var(--icon-dark);display:block}
.nav .social{position:absolute;left:639px;top:9px}

/* hero */
.hero{left:0;top:130px;width:746px;height:246px;background:linear-gradient(100deg,#3c3c3c 0%,#4f4f4f 45%,#6a6a6a 75%,#868686 100%)}
.hero-photo{left:0;top:0;width:340px;height:246px;background:
  radial-gradient(ellipse 120px 95px at 50% 47%,rgba(120,200,235,.9) 0%,rgba(40,120,170,.7) 45%,rgba(30,50,70,0) 100%),
  linear-gradient(90deg,#2c2f36 0%,#3a3f47 70%,rgba(79,79,79,0) 100%)}
.hero-title{left:377px;top:56px;font-size:14.5px;font-weight:700;color:#fff;letter-spacing:1px}
.hero-text{left:376px;top:79px;width:268px;font-size:9.6px;line-height:14px;color:#fff;letter-spacing:.2px}
.hero-btn{left:374px;top:148px;width:92px;height:25px;border:1px solid #ddd;color:#fff;font-size:10px;letter-spacing:.8px;text-align:center;line-height:23px}

/* section headings */
.section-title{font-size:12px;font-weight:400;letter-spacing:.8px;color:#333}
.section-title b{color:var(--plum);font-weight:700}
.rule{height:1px;background:var(--line)}

/* services */
.svc-title{left:45px;top:401px}
.svc-rule{left:45px;top:430px;width:632px}
.card{width:176px;top:456px}
.card-img{height:117px;border-top:5px solid var(--plum)}
.card h3{font-size:9px;font-weight:700;letter-spacing:.6px;color:var(--plum);margin:7px 0 3px 4px}
.card p{font-size:9px;line-height:11px;color:var(--muted);margin-left:3px}
.btn-small{display:inline-block;margin:9px 0 0 2px;background:var(--btn-grey);color:#fff;font-size:8px;letter-spacing:.6px;padding:3px 8px}
.carousel-arrow{width:21px;height:21px;border-radius:50%;background:var(--plum);top:511px;z-index:2}
.carousel-arrow svg{position:absolute;left:6px;top:5px}

/* news */
.news{left:0;top:694px;width:746px;height:279px;background:var(--panel)}
.news-title{left:57px;top:16px}
.news-rule{left:54px;top:42px;width:612px}
.news-img{left:54px;top:62px;width:196px;height:128px;border:4px solid #ddd;background:
  radial-gradient(ellipse 50px 40px at 45% 75%,rgba(215,205,185,.9),rgba(215,205,185,0)),
  linear-gradient(135deg,#4c6080 0%,#c9b89b 35%,#e9e6e0 60%,#9aa6b4 100%)}
.btn-plum{left:54px;top:200px;width:103px;height:22px;background:var(--plum);color:#fff;font-size:8.5px;letter-spacing:.5px;text-align:center;line-height:22px}
.btn-grey{left:165px;top:200px;width:86px;height:22px;background:var(--btn-grey);color:#fff;font-size:8.5px;letter-spacing:.5px;text-align:center;line-height:22px}
.article{width:170px}
.article h4{font-size:9px;font-weight:400;letter-spacing:.5px;color:var(--plum);margin-bottom:2px}
.article p{font-size:8.5px;line-height:13px;color:var(--text-grey);margin-left:2px;letter-spacing:.2px}
.article a{display:block;font-size:8.5px;color:var(--plum);margin:1px 0 0 3px;text-decoration:none}
.vdiv{left:462px;top:44px;width:1px;height:196px;background:#ddd}
.hdiv{left:270px;top:134px;width:396px;height:1px;background:#ddd}
.news-bottom{left:54px;top:238px;width:612px}

/* footer */
.footer-head{left:0;top:973px;width:746px;height:35px;background:linear-gradient(#ececec,#d6d6d6);border-bottom:2px solid #888}
.footer-head h5{position:absolute;top:10px;font-size:10.5px;font-weight:400;letter-spacing:.8px;color:#444}
.footer{left:0;top:1008px;width:746px;height:165px;background:var(--footer)}
.links{list-style:none;position:absolute;top:22px}
.links li{font-size:10px;letter-spacing:.8px;color:#555;height:22px}
.links li::before{content:"›";font-weight:700;margin-right:3px}
.fcontact{left:409px;top:23px;font-size:10px;color:#555;letter-spacing:.6px}
.fcontact div{display:flex;align-items:center;gap:5px;height:19px}
.fcontact .social{margin-top:4px;gap:7px}
.fcontact .social span{width:15px;height:15px;background:var(--icon-blue)}
.newsletter{left:571px;top:23px;font-size:8.5px;color:#444}
.newsletter .field{margin-top:6px;width:115px;height:20px;background:#fff;border:1px solid #bbb;font-size:8px;color:#666;padding:4px 0 0 6px}
.newsletter .submit{margin-top:7px;width:75px;height:17px;background:var(--plum);color:#fff;font-size:8.5px;letter-spacing:.5px;text-align:center;line-height:17px}
.bottombar{left:0;top:1173px;width:746px;height:27px;background:var(--footer-dark);color:#eee;font-size:7.5px}
.bottombar .copy{position:absolute;left:69px;top:9px}
.bottombar .legal{position:absolute;right:56px;top:9px}
</style>
</head>
<body>

<div class="abs topbar">
  <div class="abs contact">
    <span><svg width="9" height="7" viewBox="0 0 9 7"><rect x=".5" y=".5" width="8" height="6" fill="none" stroke="#fff"/><path d="M.5 .5 4.5 4 8.5 .5" fill="none" stroke="#fff"/></svg>youroffice@email.com</span>
    <span class="phone"><svg width="9" height="9" viewBox="0 0 9 9"><rect width="9" height="9" rx="1.5" fill="#fff"/><path d="M2.5 2c0 3 1.5 4.5 4.5 5" stroke="#8e1a5a" stroke-width="1.4" fill="none"/></svg>02-1234-5678</span>
  </div>
  <div class="abs btn-signin">Sign-in</div>
  <div class="abs btn-signup">Sign-up</div>
</div>

<div class="abs header">
  <div class="abs brand"><span class="brand-mark"></span><span class="brand-name">plumbrook</span></div>
  <div class="abs search">Keyword Search...
    <svg width="9" height="9" viewBox="0 0 9 9"><circle cx="3.5" cy="3.5" r="2.6" fill="none" stroke="#777" stroke-width="1.2"/><path d="M5.5 5.5 8.5 8.5" stroke="#777" stroke-width="1.4"/></svg>
  </div>
</div>

<nav class="abs nav">
  <ul>
    <li>HOME</li><li>ABOUT US</li><li>WHAT WE DO</li><li>NEWS BLOG</li><li>ARTICLES</li><li>CLIENTS</li><li>PARTNERS</li>
  </ul>
  <div class="social" aria-label="Social links"><span></span><span></span><span></span></div>
</nav>

<section class="abs hero">
  <div class="abs hero-photo" role="img" aria-label="Businessman holding a glowing globe of connected devices and data"></div>
  <h1 class="abs hero-title">WELCOME TO PLUMBROOK</h1>
  <p class="abs hero-text">Plumbrook was established with a specific aim: to consistently deliver an advanced and comprehensive IT service for ambitious growing companies across all industry sectors.</p>
  <div class="abs hero-btn">READ MORE</div>
</section>

<h2 class="abs section-title svc-title">OUR <b>SERVICES</b></h2>
<div class="abs rule svc-rule"></div>

<div class="abs carousel-arrow" style="left:52px"><svg width="9" height="11" viewBox="0 0 9 11"><path d="M7 1 2 5.5 7 10" fill="none" stroke="#fff" stroke-width="2.4"/></svg></div>
<div class="abs carousel-arrow" style="left:650px"><svg width="9" height="11" viewBox="0 0 9 11"><path d="M2 1 7 5.5 2 10" fill="none" stroke="#fff" stroke-width="2.4"/></svg></div>

<article class="abs card" style="left:65px">
  <div class="card-img" role="img" aria-label="Laptop with glowing world map and network lines" style="background:radial-gradient(ellipse 70px 45px at 50% 40%,#7cc3f0,rgba(60,140,210,0)),linear-gradient(135deg,#0d3f7a,#2f7fc6 50%,#0b2e5c)"></div>
  <h3>IT SUPPORT &amp; MANAGEMENT</h3>
  <p>Lorem ipsum dolor sit amet, consecte-tur adipiscing elit. Ut felis ligula, dignissim sit amet interdum.</p>
  <span class="btn-small">READ MORE ›</span>
</article>
<article class="abs card" style="left:274px">
  <div class="card-img" role="img" aria-label="Hand holding a tablet with virtual network icons" style="background:radial-gradient(ellipse 40px 30px at 45% 50%,#c8d2dc,rgba(150,160,170,0)),linear-gradient(90deg,#5a5f66,#44484e 60%,#202226)"></div>
  <h3>VIRTUALIZATION</h3>
  <p>Lorem ipsum dolor sit amet, consecte-tur adipiscing elit. Ut felis ligula, dignissim sit amet interdum non.</p>
  <span class="btn-small">READ MORE ›</span>
</article>
<article class="abs card" style="left:483px">
  <div class="card-img" role="img" aria-label="Laptop with metal gears and calliper" style="background:radial-gradient(ellipse 60px 35px at 65% 40%,#8d9197,rgba(180,184,190,0)),linear-gradient(160deg,#fafafa,#c9ccd0 60%,#eeeeee)"></div>
  <h3>CAD SERVICES</h3>
  <p>Lorem ipsum dolor sit amet, consecte-tur adipiscing elit. Ut felis ligula, dignissim sit amet interdum</p>
  <span class="btn-small">READ MORE ›</span>
</article>

<section class="abs news">
  <h2 class="abs section-title news-title">LATEST <b>NEWS</b></h2>
  <div class="abs rule news-rule"></div>
  <div class="abs news-img" role="img" aria-label="Team working at a desk with laptop, papers and coffee"></div>
  <div class="abs btn-plum">VIEW ALL ARTICLES</div>
  <div class="abs btn-grey">CONTACT US</div>
  <div class="abs vdiv"></div>
  <div class="abs hdiv"></div>

  <div class="abs article" style="left:294px;top:62px">
    <h4>TITLE OF THE ARTICLE GOES HERE</h4>
    <p>Lorem ipsum dolor sit amet, consecte-tur adipiscing elit. Phasellus tincidunt tellus leo, sodales vestibulum urna.</p>
    <a>Read more →</a>
  </div>
  <div class="abs article" style="left:501px;top:62px">
    <h4>TITLE OF THE ARTICLE GOES HERE</h4>
    <p>Lorem ipsum dolor sit amet, consecte-tur adipiscing elit. Phasellus tincidunt tellus leo, sodales vestibulum urna.</p>
    <a>Read more →</a>
  </div>
  <div class="abs article" style="left:294px;top:151px">
    <h4>TITLE OF THE ARTICLE GOES HERE</h4>
    <p>Lorem ipsum dolor sit amet, consecte-tur adipiscing elit. Phasellus tincidunt tellus leo, sodales vestibulum urna.</p>
    <a>Read more →</a>
  </div>
  <div class="abs article" style="left:501px;top:151px">
    <h4>TITLE OF THE ARTICLE GOES HERE</h4>
    <p>Lorem ipsum dolor sit amet, consecte-tur adipiscing elit. Phasellus tincidunt tellus leo, sodales vestibulum urna.</p>
    <a>Read more →</a>
  </div>
  <div class="abs rule news-bottom"></div>
</section>

<div class="abs footer-head">
  <h5 style="left:73px">Who we are</h5>
  <h5 style="left:243px">What we offer</h5>
  <h5 style="left:406px">Contact us</h5>
  <h5 style="left:574px">Newsletter Signup</h5>
</div>

<footer class="abs footer">
  <ul class="links" style="left:72px"><li>Link here</li><li>Link here</li><li>Link here</li><li>Link here</li><li>Link here</li></ul>
  <ul class="links" style="left:243px"><li>Link here</li><li>Link here</li><li>Link here</li><li>Link here</li><li>Link here</li></ul>
  <div class="abs fcontact">
    <div><svg width="11" height="8" viewBox="0 0 11 8"><rect width="11" height="8" fill="#eee"/><path d="M0 0 5.5 4.5 11 0" fill="none" stroke="#bbb"/></svg>Youroffice@email.com</div>
    <div><svg width="11" height="8" viewBox="0 0 11 8"><rect width="11" height="8" rx="1" fill="#eee"/></svg>02-1234-456</div>
    <div class="social" aria-label="Social links"><span></span><span></span><span></span></div>
  </div>
  <div class="abs newsletter">
    <div>Subscribe to get updates</div>
    <div class="field">Email address</div>
    <div class="submit">SUBMIT</div>
  </div>
</footer>

<div class="abs bottombar">
  <span class="copy">Copyright © 2014 Plumbrook All rights reserved</span>
  <span class="legal">FAQ &nbsp;-&nbsp; Sitemap &nbsp;-&nbsp; Privacy Policy</span>
</div>

</body>
</html>
```